Zuvo Decor

There is a sample provided with the arabic text of the business card. please copy paste the same text and the same Logo (The two triangles) Just try to incorproate the Brown background attached (you are free to change the colors) Id like the colors to be mainly shades of black and red.

```html
<!DOCTYPE html>
<html lang="ar">
<head>
<meta charset="utf-8">
<title>Zuvo Decor – Business Card</title>
<link href="https://fonts.googleapis.com/css2?family=Tajawal:wght@400;500&family=Aref+Ruqaa:wght@400;700&family=Roboto:wght@400&display=swap" rel="stylesheet">
<style>
  :root {
    --page-bg: #ece9e6;
    --card-red: #cf1f45;
    --card-red-deep: #b8173a;
    --card-red-light: #e0355a;
    --card-black: #262724;
    --stripe-white: #ffffff;
    --text-white: #ffffff;
    --bullet-dark: #1f1f1f;
  }
  * { margin: 0; padding: 0; box-sizing: border-box; }
  html, body {
    width: 1125px;
    height: 1200px;
    overflow: hidden;
    background: var(--page-bg);
  }
  .canvas {
    position: relative;
    width: 1125px;
    height: 1200px;
  }
  .card {
    position: absolute;
    left: 170px;
    width: 828px;
    height: 472px;
    overflow: hidden;
    box-shadow: 0 3px 8px rgba(0, 0, 0, 0.25);
  }
  .card--front { top: 106px; }
  .card--back  { top: 639px; }

  .texture {
    position: absolute;
    inset: 0;
    background:
      radial-gradient(ellipse at 35% 30%, var(--card-red-light) 0%, transparent 60%),
      linear-gradient(160deg, var(--card-red) 0%, var(--card-red-deep) 100%);
  }
  .front-brand-panel {
    position: absolute;
    left: 0; top: 0;
    width: 405px;
    height: 100%;
  }
  .divider-stripe {
    position: absolute;
    left: 405px; top: 0;
    width: 14px;
    height: 100%;
    background: var(--stripe-white);
  }
  .front-info-panel {
    position: absolute;
    left: 419px; top: 0; right: 0;
    height: 100%;
    background: var(--card-black);
  }
  .pointer {
    position: absolute;
    left: 419px;
    top: 102px;
  }
  .brand-name {
    position: absolute;
    left: 0; width: 405px;
    top: 205px;
    text-align: center;
    font-family: "Tajawal", sans-serif;
    font-weight: 500;
    font-size: 46px;
    letter-spacing: 1px;
    color: var(--text-white);
  }
  .person {
    position: absolute;
    right: 120px;
    top: 78px;
    text-align: center;
    color: var(--text-white);
    font-family: "Aref Ruqaa", serif;
  }
  .person__name { font-size: 28px; font-weight: 700; line-height: 1.2; }
  .person__title { font-size: 20px; line-height: 1.2; }
  .credentials {
    list-style: none;
    direction: rtl;
    font-family: "Tajawal", sans-serif;
    font-size: 24px;
    line-height: 27.5px;
    color: var(--text-white);
  }
  .front-info-panel .credentials {
    position: absolute;
    right: 126px;
    top: 244px;
  }
  .phone {
    position: absolute;
    right: 105px;
    top: 375px;
    display: flex;
    align-items: center;
    gap: 6px;
    font-family: "Roboto", sans-serif;
    font-size: 22px;
    color: var(--text-white);
  }
  .back-columns {
    position: absolute;
    top: 163px;
    right: 85px;
    display: flex;
    gap: 70px;
    direction: rtl;
  }
  .back-columns .credentials { line-height: 33px; font-size: 25px; }
  .back-columns .credentials li {
    position: relative;
    padding-right: 20px;
  }
  .back-columns .credentials li::before {
    content: "";
    position: absolute;
    right: 0;
    top: 14px;
    width: 9px; height: 9px;
    border-radius: 50%;
    background: var(--bullet-dark);
  }
</style>
</head>
<body>
<main class="canvas">

  <section class="card card--front">
    <div class="front-brand-panel">
      <div class="texture" role="img" aria-label="Red background with a soft square-and-dot grid pattern"></div>
      <div class="brand-name">Zuvo Decor</div>
    </div>
    <div class="divider-stripe"></div>
    <div class="front-info-panel">
      <div class="person">
        <div class="person__name">المهندس / سامر نبيل الراشد</div>
        <div class="person__title">أستاذ جامعي</div>
      </div>
      <ul class="credentials">
        <li>ماجستير هندسة ديكور</li>
        <li>دبلوم عالي فن تشكيلي</li>
        <li>أكاديمية الفنون (روما)</li>
        <li>استشارات هندسية - فنية</li>
      </ul>
      <div class="phone">
        <svg width="18" height="20" viewBox="0 0 24 24" aria-hidden="true">
          <path fill="#fff" d="M6.6 10.8a15.2 15.2 0 0 0 6.6 6.6l2.2-2.2a1 1 0 0 1 1-.25 11.4 11.4 0 0 0 3.6.57 1 1 0 0 1 1 1V20a1 1 0 0 1-1 1A17 17 0 0 1 3 4a1 1 0 0 1 1-1h3.5a1 1 0 0 1 1 1c0 1.25.2 2.45.57 3.57a1 1 0 0 1-.25 1z"/>
        </svg>
        <span>30125478 / 60124589</span>
      </div>
    </div>
    <svg class="pointer" width="20" height="22" viewBox="0 0 20 22" aria-hidden="true">
      <polygon points="0,0 20,11 0,22" fill="var(--stripe-white)"/>
    </svg>
  </section>

  <section class="card card--back">
    <div class="texture" role="img" aria-label="Red background with a soft square-and-dot grid pattern"></div>
    <div class="back-columns">
      <ul class="credentials">
        <li>ماجستير هندسة ديكور</li>
        <li>دبلوم عالي فن تشكيلي</li>
        <li>أكاديمية الفنون (روما)</li>
        <li>استشارات هندسية - فنية</li>
      </ul>
      <ul class="credentials">
        <li>ماجستير هندسة ديكور</li>
        <li>دبلوم عالي فن تشكيلي</li>
        <li>أكاديمية الفنون (روما)</li>
        <li>استشارات هندسية - فنية</li>
      </ul>
    </div>
  </section>

</main>
</body>
</html>
```